Computer ID tag

We need a small tag to place on computers that we work on. Just a little bit of information needs to be on it but we need it to be catchy.

Industry/Entity Type

Computer

Requirements
Must have
• Velmoro,inc logo or variation, 1(800)562-9041, Velmoroinc.example

```html
<!DOCTYPE html>
<html lang="en">
<head>
<meta charset="utf-8">
<title>Velmoro,inc – Computer ID Tag</title>
<link rel="stylesheet" href="https://fonts.googleapis.com/css2?family=Lato:wght@400;700&family=Oswald:wght@300&display=swap">
<style>
  :root {
    --page-bg: #d9e8f6;
    --tag-white: #ffffff;
    --tag-blue: #5190cd;
    --tag-navy: #1b3a8c;
    --name-navy: #1f2a5c;
    --accent-red: #c6262e;
    --phone-tint: #d3e0f2;
  }
  html, body {
    margin: 0;
    padding: 0;
    width: 1200px;
    height: 1199px;
    overflow: hidden;
    background: var(--page-bg);
  }
  .id-tag {
    position: absolute;
    left: 100px;
    top: 273px;
    width: 1000px;
    height: 652px;
    background: var(--tag-white);
    overflow: hidden;
  }
  .id-tag__waves {
    position: absolute;
    inset: 0;
    width: 100%;
    height: 100%;
  }
  .wave-fill { fill: var(--tag-blue); }
  .wave-edge { fill: var(--tag-navy); }
  .brand-name {
    position: absolute;
    left: 62px;
    top: 150px;
    margin: 0;
    font-family: "Lato", sans-serif;
    font-weight: 700;
    font-size: 88px;
    line-height: 1;
    color: var(--name-navy);
  }
  .contact-phone {
    position: absolute;
    right: 50px;
    top: 440px;
    display: flex;
    align-items: center;
    gap: 14px;
    font-family: "Oswald", sans-serif;
    font-weight: 300;
    font-size: 46px;
    line-height: 1;
    color: var(--phone-tint);
  }
  .contact-phone svg { width: 34px; height: 34px; fill: var(--phone-tint); }
  .contact-web {
    position: absolute;
    right: 48px;
    top: 540px;
    font-family: "Lato", sans-serif;
    font-weight: 400;
    font-size: 56px;
    line-height: 1;
    color: var(--accent-red);
  }
</style>
</head>
<body>
  <main class="id-tag">
    <svg class="id-tag__waves" viewBox="0 0 590 385" preserveAspectRatio="none" aria-hidden="true">
      <path class="wave-fill" d="M0,318 C170,370 440,330 535,0 L590,0 L590,385 L0,385 Z"/>
      <path class="wave-edge" d="M0,302 C165,360 420,322 520,0 L537,0 C440,338 170,372 0,320 Z"/>
    </svg>

    <h1 class="brand-name">Velmoro,inc</h1>

    <div class="contact-phone">
      <svg viewBox="0 0 24 24" aria-hidden="true">
        <path d="M6.6 10.8c1.4 2.8 3.8 5.1 6.6 6.6l2.2-2.2c.3-.3.7-.4 1-.2 1.1.4 2.3.6 3.6.6.6 0 1 .4 1 1V20c0 .6-.4 1-1 1C10.6 21 3 13.4 3 4c0-.6.4-1 1-1h3.5c.6 0 1 .4 1 1 0 1.3.2 2.5.6 3.6.1.3 0 .7-.2 1z"/>
      </svg>
      <span>1(800)562-9041</span>
    </div>

    <div class="contact-web">Velmoroinc.example</div>
  </main>
</body>
</html>
```